Business Card with Logo and Company Name.

I would like a business card design that has both my logo and company name. The 2R logo was one part- now I would like the entire Company Name.

DOUBLE R CONTRACTING SERVICES

I have consulted with my team and we have went over several ideas for the last few weeks. We all love the 2R logo. Great for branding. What we have thought of in regards to the company name to tie into it is giving focus to font selection. We love the idea of DOUBLE R being a larger font and maybe making CONTRACTING SERVICES a larger font. Much like one would for a Slogan Line and font when designing.

I hope I’m communicating this correctly and not causing confusion. If need be I can mock up or sketch an idea and send. Just let me know.

**** I just noticed an area to upload an image. I uploaded one that was used as an idea*****

```html
<!DOCTYPE html>
<html lang="en">
<head>
<meta charset="utf-8">
<title>Double R Contracting Services – Business Card</title>
<link href="https://fonts.googleapis.com/css2?family=Saira+Semi+Condensed:wght@800&family=PT+Serif&family=Open+Sans:wght@400&display=swap" rel="stylesheet">
<style>
  :root {
    --page: #ffffff;
    --ink-dark: #151920;
    --slate-light: #363c45;
    --slate-mid: #262b33;
    --slate-deep: #14171c;
    --panel-light: #3c424b;
    --panel-dark: #1c1f25;
    --rule-light: #8c9096;
    --rule-dark: #9a9a9a;
    --text-white: #ffffff;
    --text-muted: #8b8f95;
  }
  html, body {
    margin: 0;
    width: 1200px;
    height: 998px;
    overflow: hidden;
    background: var(--page);
  }
  .canvas { position: relative; width: 1200px; height: 998px; }

  .card {
    position: absolute;
    width: 539px;
    height: 307px;
    overflow: hidden;
  }

  /* Front */
  .card-front {
    left: 324px; top: 131px;
    background: linear-gradient(225deg, var(--slate-deep) 0%, var(--slate-mid) 50%, var(--slate-light) 100%);
  }
  .logo-row {
    position: absolute;
    display: flex;
    align-items: center;
  }
  .logo-rule { flex: 1; height: 1px; }
  .logo-name {
    font-family: "Saira Semi Condensed", sans-serif;
    font-weight: 800;
    line-height: 1;
    white-space: nowrap;
  }
  .tagline {
    position: absolute;
    font-family: "PT Serif", serif;
    white-space: nowrap;
    text-align: center;
  }
  .card-front .logo-row { left: 0; right: 0; top: 118px; height: 70px; }
  .card-front .logo-rule { background: var(--rule-light); }
  .card-front .logo-name {
    color: var(--text-white);
    font-size: 70px;
    padding: 0 12px;
    transform: translateY(-16px);
  }
  .card-front .tagline {
    left: 0; right: 0; top: 177px;
    color: var(--text-white);
    font-size: 15px;
    letter-spacing: 3.4px;
  }

  /* Back */
  .card-back {
    left: 326px; top: 534px;
    background: var(--page);
    box-shadow: 0 1px 4px rgba(0,0,0,0.35);
  }
  .card-back .logo-row { left: 0; width: 266px; top: 127px; height: 46px; }
  .card-back .logo-rule { background: var(--rule-dark); }
  .card-back .logo-name {
    color: var(--ink-dark);
    font-size: 46px;
    padding: 0 8px;
    transform: translateY(-10px);
  }
  .card-back .tagline {
    left: 0; width: 290px; top: 171px;
    color: var(--ink-dark);
    font-size: 10.5px;
    letter-spacing: 2.3px;
  }
  .block { position: absolute; }
  .block-top {
    left: 241px; right: 0; top: 0; height: 82px;
    background: linear-gradient(90deg, var(--slate-mid), var(--slate-deep));
  }
  .block-contact {
    left: 283px; right: 0; top: 82px; height: 144px;
    background: linear-gradient(90deg, var(--panel-light), var(--panel-dark));
  }
  .block-bottom {
    left: 241px; right: 0; top: 226px; bottom: 0;
    background: linear-gradient(90deg, var(--slate-mid), var(--slate-deep));
  }
  .person-name, .person-role, .contact-line {
    position: absolute;
    font-family: "Open Sans", sans-serif;
    font-weight: 400;
    white-space: nowrap;
    line-height: 1;
  }
  .person-name { left: 263px; top: 28px; font-size: 23px; letter-spacing: 4.5px; color: var(--text-white); }
  .person-role { left: 261px; top: 57px; font-size: 13.5px; letter-spacing: 3px; color: var(--text-muted); }
  .contact-line { left: 309px; font-size: 11px; letter-spacing: 2px; color: var(--text-white); }
</style>
</head>
<body>
<main class="canvas">
  <section class="card card-front" aria-label="Business card front">
    <div class="logo-row">
      <span class="logo-rule"></span>
      <span class="logo-name">DOUBLE R</span>
      <span class="logo-rule"></span>
    </div>
    <p class="tagline" style="margin:0">CONTRACTING SERVICES</p>
  </section>

  <section class="card card-back" aria-label="Business card back">
    <div class="logo-row">
      <span class="logo-rule"></span>
      <span class="logo-name">DOUBLE R</span>
      <span class="logo-rule"></span>
    </div>
    <p class="tagline" style="margin:0">CONTRACTING SERVICES</p>

    <div class="block block-top"></div>
    <div class="block block-contact"></div>
    <div class="block block-bottom"></div>

    <span class="person-name">SAM CARTER</span>
    <span class="person-role">ARCHITECT</span>

    <span class="contact-line" style="top:121px">INFO@BUILDMAILER.COM</span>
    <span class="contact-line" style="top:148px">+123-55501234</span>
    <span class="contact-line" style="top:164px">+123-55501234</span>
    <span class="contact-line" style="top:194px">WWW.BUILDMAILER.COM</span>
  </section>
</main>
</body>
</html>
```